Luxury Business Card Design for High-End Window Treatments

Gilded Slatworks
Custom Plantation Shutters & Architectural Shading Systems

⸻

BACK

Daniel Ferrowitz
Owner

Custom Interior & Exterior Window Treatments

919-555-0187
gildedslatworks.example

I have included a picture that I’m hoping we can use on the back, but I’m also wondering if you can get rid of the ladder? Should we get rid of shutters , shades and blinds underneath Gilded Slatworks?

Target Market(s)

High-end residential homeowners, custom home builders, architects, interior designers, and luxury renovation clients seeking premium plantation shutters and motorized architectural shading systems.

Industry/Entity Type

Custom Window treatments

Contact Information for Business Card

Front Gilded Slatworks Custom Plantation Shutters Motorized Architectural Shading Systems BACK Daniel Ferrowitz Owner 919-555-0187 GildedSlatworks.example Custom Interior & Exterior Window Treatments By Appointment

Requirements
Nice to have
• Not 100% sure on nice to halves or the color but you can definitely check out my website to get a better understanding of what I’m trying to do

```html
<!DOCTYPE html>
<html lang="en">
<head>
<meta charset="utf-8">
<title>Gilded Slatworks – Business Card</title>
<link href="https://fonts.googleapis.com/css2?family=Poppins:wght@400;600&display=swap" rel="stylesheet">
<style>
  :root {
    --backdrop: #2b2b2b;
    --card: #151515;
    --gold: #c9a544;
    --gold-soft: #b8953a;
    --emboss: #262626;
    --ink-light: #f2f2f2;
    --sky: #6fa2d8;
    --porch: #3c4048;
  }
  * { box-sizing: border-box; margin: 0; padding: 0; }
  html, body {
    width: 1200px; height: 875px; overflow: hidden;
    background: var(--backdrop);
    font-family: "Poppins", sans-serif;
  }
  .sheet {
    width: 1200px; height: 875px;
    display: flex; flex-direction: column; align-items: center; justify-content: center;
    gap: 40px;
  }
  .card {
    position: relative;
    width: 700px; height: 400px;
    background: var(--card);
    border-radius: 22px;
    border: 3px solid var(--gold);
    overflow: hidden;
  }
  .card-front { display: flex; align-items: center; justify-content: center; }
  .wordmark {
    font-weight: 600;
    line-height: 1.05;
    letter-spacing: 0.5px;
  }
  .wordmark-emboss { color: var(--emboss); font-size: 70px; text-align: center; }
  .card-back .identity {
    position: absolute; left: 60px; top: 70px;
  }
  .wordmark-gold { color: var(--gold); font-size: 52px; }
  .person { margin-top: 34px; }
  .person-name { color: var(--gold); font-weight: 600; font-size: 26px; line-height: 1.1; }
  .person-role { color: var(--ink-light); font-size: 15px; }
  .contact { margin-top: 18px; list-style: none; }
  .contact li {
    display: flex; align-items: center; gap: 10px;
    color: var(--ink-light); font-size: 17px; line-height: 1.6;
  }
  .contact .phone { font-weight: 600; }
  .contact svg { width: 15px; height: 15px; flex: none; }
  .photo-frame { position: absolute; right: 0; top: 0; width: 700px; height: 400px; pointer-events: none; }
</style>
</head>
<body>
<main class="sheet">
  <section class="card card-front" aria-label="Card front">
    <h1 class="wordmark wordmark-emboss">Gilded<br>Slatworks</h1>
  </section>

  <section class="card card-back" aria-label="Card back">
    <svg class="photo-frame" viewBox="0 0 700 400" aria-hidden="false">
      <defs>
        <linearGradient id="porchTones" x1="0" y1="0" x2="0" y2="1">
          <stop offset="0" stop-color="var(--sky)"/>
          <stop offset="0.35" stop-color="#8fa08a"/>
          <stop offset="0.6" stop-color="var(--porch)"/>
          <stop offset="1" stop-color="#4d5a3c"/>
        </linearGradient>
      </defs>
      <g role="img" aria-label="Photo of a house porch fitted with exterior shades">
        <rect x="480" y="-90" width="360" height="360" rx="70"
              transform="rotate(45 660 90)" fill="url(#porchTones)"/>
      </g>
    </svg>
    <div class="identity">
      <h2 class="wordmark wordmark-gold">Gilded<br>Slatworks</h2>
      <div class="person">
        <p class="person-name">Daniel Ferrowitz</p>
        <p class="person-role">Owner</p>
      </div>
      <ul class="contact">
        <li class="phone">
          <svg viewBox="0 0 16 16"><path fill="var(--gold)" d="M3 1h3l1.5 4-2 1.2a9 9 0 0 0 4.3 4.3L11 8.5l4 1.5v3a2 2 0 0 1-2 2A12 12 0 0 1 1 3a2 2 0 0 1 2-2z"/></svg>
          919-555-0187
        </li>
        <li>
          <svg viewBox="0 0 16 16"><circle cx="8" cy="8" r="6.5" fill="none" stroke="var(--gold)" stroke-width="1.6"/><path d="M1.5 8h13M8 1.5c-3 3.5-3 9.5 0 13M8 1.5c3 3.5 3 9.5 0 13" fill="none" stroke="var(--gold)" stroke-width="1.2"/></svg>
          gildedslatworks.example
        </li>
      </ul>
    </div>
  </section>
</main>
</body>
</html>
```